Swiss VPS hosting website for local hosting provider

Hi,

Need a new website which includes the same pages as todays website under https://www.alpvexa.ch

Those include:
Homepage
Product pages
Blog
Contact page

There should be a mobile version as well

Coding will be done on drupal.

Looking for a fresh design which fit to VPS hosting. Other examples are corvimbo.ch which I very much like. Very plain and not a lot of not needed stuff.

Target Market(s)

Switzerland, VPS Hosting

Industry/Entity Type

Product

Number of Pages Required

4 page

Font styles to use
Sans Serif

Requirements
Must have
• Same sites as the original site

```html
<!DOCTYPE html>
<html lang="en">
<head>
<meta charset="utf-8">
<title>Peakhost – VPS Hosting Solution</title>
<link href="https://fonts.googleapis.com/css2?family=Montserrat:wght@400;500;600;700&display=swap" rel="stylesheet">
<style>
:root{
  --stage:#c0c0c0;
  --page:#ffffff;
  --ink:#2b2f36;
  --muted:#8a8f96;
  --dark:#262d36;
  --green:#2ecc71;
  --blue:#2bb3d9;
  --red:#f0574f;
  --orange:#f39c12;
  --row:#f1f1f1;
  --icon:#8e97a3;
}
*{margin:0;padding:0;box-sizing:border-box}
html,body{width:960px;height:1200px;overflow:hidden;background:var(--stage);font-family:'Montserrat',Arial,sans-serif;color:var(--ink)}
.page{position:absolute;left:221px;top:0;width:537px;height:1200px;background:var(--page);overflow:hidden}
.abs{position:absolute}
.center{text-align:center}

/* hero */
.hero{left:0;top:0;width:537px;height:214px;background:linear-gradient(180deg,#1f262e 0%,#323b46 55%,#2a323c 100%)}
.hero-texture{left:0;top:0;width:537px;height:214px;background:repeating-linear-gradient(90deg,rgba(255,255,255,.03) 0 2px,transparent 2px 34px),linear-gradient(180deg,rgba(0,0,0,.25),rgba(0,0,0,0))}
.brand{left:78px;top:13px;height:17px;display:flex;align-items:center;gap:5px;color:#fff;font-size:9px;font-weight:600}
.brand-mark{width:8px;height:8px;background:var(--green)}
.nav{left:174px;top:17px;display:flex;gap:12px;font-size:4.6px;font-weight:600;color:#fff;letter-spacing:.2px}
.nav .signup{background:var(--green);padding:2px 9px;margin-top:-2px;height:9px}
.hero-title{left:0;width:537px;top:74px;font-size:23px;font-weight:700;color:#fff;letter-spacing:-.5px}
.hero-sub{left:80px;width:377px;top:109px;font-size:9.6px;line-height:12.5px;color:#e4e8ec}
.btn{top:147px;height:20px;width:97px;font-size:6.8px;color:#fff;line-height:20px;text-align:center}
.btn-green{left:167px;background:var(--green)}
.btn-blue{left:272px;background:var(--blue)}

/* key points */
.point{width:110px;text-align:center}
.point svg{display:block;margin:0 auto}
.point h3{font-size:6.6px;font-weight:600;margin-top:6px}
.point p{font-size:4.3px;line-height:7.4px;color:var(--muted);margin-top:4px}

.section-title{left:0;width:537px;font-size:13.5px;font-weight:600;text-align:center}
.section-sub{left:0;width:537px;font-size:7.6px;color:#555;text-align:center}

/* feature grid */
.feature{width:160px}
.feature h4{font-size:6.6px;font-weight:600}
.feature p{font-size:4.2px;line-height:7.5px;color:var(--muted);margin-top:4px}

/* layout block */
.servers{left:89px;top:530px;width:130px;height:96px;background:radial-gradient(ellipse at 50% 40%,#3a5a86 0%,#1c2129 55%,#fff 80%)}
.lay-title{left:240px;top:529px;font-size:13px;font-weight:600}
.lay-sub{left:240px;top:545px;font-size:7.6px;color:#555}
.lay-text{left:240px;top:562px;width:218px;font-size:4.2px;line-height:7.5px;color:var(--muted)}
.tick{font-size:4.8px;font-weight:600;display:flex;align-items:center;gap:6px;color:#444}

/* testimonials */
.avatar{width:29px;height:29px;border-radius:50%;background:#d6d6d6}
.quote{width:110px;font-size:4.2px;line-height:7.4px;font-style:italic;color:var(--muted);text-align:center}
.author{width:110px;font-size:4.3px;font-weight:600;text-align:center}
.partner{top:780px;font-size:11px;color:#8a8a8a}

/* pricing */
.plan{top:870px;width:89px;height:175px}
.plan-head{position:absolute;top:22px;left:0;width:89px;height:40px;background:var(--dark);color:#fff;text-align:center}
.plan-head h5{font-size:8px;font-weight:600;margin-top:20px}
.plan-head span{display:block;font-size:4.2px;color:#a8b0ba;margin-top:1px}
.price{position:absolute;top:1px;left:23px;width:42px;height:42px;border-radius:50%;color:#fff;font-size:14px;font-weight:600;line-height:42px;text-align:center;background:var(--green)}
.plan-list{position:absolute;top:62px;left:0;width:89px;height:95px;background:var(--row);list-style:none;padding-top:7px}
.plan-list li{font-size:4.6px;color:#666;text-align:center;height:14.4px;line-height:14.4px}
.plan-btn{position:absolute;top:157px;left:0;width:89px;height:18px;background:var(--green);color:#fff;font-size:7.4px;font-weight:600;line-height:18px;text-align:center}
.plan.hot .price,.plan.hot .plan-btn{background:var(--red)}
.plan.hot .plan-list li{color:#444;font-weight:500}

/* footer */
.footer{left:0;top:1098px;width:537px;height:102px;background:var(--dark)}
.fcol{top:24px;font-size:4.2px;line-height:8px;color:#d0d5db}
.fcol h6{font-size:4.2px;font-weight:500;color:#6e7782;margin-bottom:2px}
.chat{left:401px;top:32px;width:56px;height:11px;background:var(--green);color:#fff;font-size:4.4px;font-weight:600;line-height:11px;text-align:center}
.fbrand{left:421px;top:76px;width:36px;height:9px;color:#5b6470;font-size:4.6px;line-height:9px;text-align:right;font-weight:500}
</style>
</head>
<body>
<div class="page">

  <header class="abs hero">
    <div class="abs hero-texture" role="img" aria-label="Dimmed photo of server racks in a data centre"></div>
    <div class="abs brand"><span class="brand-mark"></span>Peakhost</div>
    <nav class="abs nav">
      <span>HOME</span><span>FEATURES ⌄</span><span>TESTIMONIALS</span><span>PRICING</span><span>BLOG</span><span>CONTACT</span><span>LOGIN</span><span class="signup">SIGNUP</span>
    </nav>
    <h1 class="abs hero-title center">VPS Hosting Solution</h1>
    <p class="abs hero-sub center">Peakhost is a grid based responsive minimal, flat and afforable hosting template with easy customization and great support</p>
    <a class="abs btn btn-green">Explore Features</a>
    <a class="abs btn btn-blue">Plans and Pricing</a>
  </header>

  <section>
    <div class="abs point" style="left:84px;top:228px">
      <svg width="28" height="28" viewBox="0 0 28 28"><path d="M14 2 L25 6 V13 C25 20 20 24 14 26 C8 24 3 20 3 13 V6 Z" fill="var(--green)"/><path d="M8.5 14 L12.5 18 L19.5 10" stroke="#fff" stroke-width="3" fill="none" stroke-linecap="round" stroke-linejoin="round"/></svg>
      <h3>Secure &amp; Reliable</h3>
      <p>Peakhost servers are having high physical security and power redundancy Your data will be secure with us.</p>
    </div>
    <div class="abs point" style="left:213px;top:228px">
      <svg width="28" height="28" viewBox="0 0 28 28"><path d="M14 2 C19 6 20 12 18 19 H10 C8 12 9 6 14 2 Z" fill="#e8453c"/><path d="M10 14 L5 20 L10 19 Z M18 14 L23 20 L18 19 Z" fill="#c0392b"/><circle cx="14" cy="11" r="2.6" fill="#fff"/><path d="M12 21 H16 L14 26 Z" fill="#e8453c"/></svg>
      <h3>Super Fast</h3>
      <p>With our ultra mordern servers and optical cables, your data will be transfered to end user in milliseconds.</p>
    </div>
    <div class="abs point" style="left:342px;top:228px">
      <svg width="28" height="28" viewBox="0 0 28 28"><rect x="9" y="9" width="17" height="12" rx="5" fill="#e67e22"/><path d="M20 20 L24 25 L17 21 Z" fill="#e67e22"/><rect x="2" y="4" width="17" height="12" rx="5" fill="var(--orange)"/><path d="M6 15 L4 20 L10 16 Z" fill="var(--orange)"/><path d="M6 9 H15 M6 12 H12" stroke="#fff" stroke-width="1.5" stroke-linecap="round"/></svg>
      <h3>Customer Support</h3>
      <p>We have a dedicated team of support for sales and support to help you in anytime. You can also chat with us.</p>
    </div>
  </section>

  <h2 class="abs section-title" style="top:324px">More Features</h2>
  <p class="abs section-sub" style="top:340px">You will get lot of features with peakhost</p>

  <section>
    <svg class="abs" style="left:79px;top:367px" width="24" height="24" viewBox="0 0 24 24"><circle cx="12" cy="12" r="7" fill="none" stroke="var(--icon)" stroke-width="4" stroke-dasharray="3.2 2.3"/><circle cx="12" cy="12" r="6" fill="none" stroke="var(--icon)" stroke-width="3"/></svg>
    <div class="abs feature" style="left:110px;top:367px"><h4>Instant Setup</h4><p>As soon as you make a successful payment via PayWell or QuickCheckout, your web hosting and domain names will be activated immediately. No waiting time whatsoever.</p></div>

    <svg class="abs" style="left:272px;top:367px" width="24" height="24" viewBox="0 0 24 24"><path d="M3 12 H21 V21 H3 Z" fill="none" stroke="var(--icon)" stroke-width="2"/><path d="M3 16 H21" stroke="var(--icon)" stroke-width="1.5"/><path d="M12 2 V12 M8 8 L12 12 L16 8" stroke="var(--icon)" stroke-width="2.4" fill="none"/></svg>
    <div class="abs feature" style="left:304px;top:367px"><h4>Constant Backups</h4><p>Your hosting account is backed up 4 times a day as standard, with our backup integration. We use dedicated backup servers, providing fast &amp; easy individual file rollback abilities.</p></div>

    <svg class="abs" style="left:79px;top:418px" width="24" height="18" viewBox="0 0 24 18"><path d="M8 3 L2 9 L8 15 M16 3 L22 9 L16 15" stroke="var(--icon)" stroke-width="2" fill="none"/></svg>
    <div class="abs feature" style="left:110px;top:417px"><h4>Version Control Support</h4><p>Web Developers love using version control systems. All of our hosting accounts can use common version control command line tools on our servers. Simply request SSH access to get started.</p></div>

    <svg class="abs" style="left:272px;top:416px" width="24" height="24" viewBox="0 0 24 24"><circle cx="12" cy="12" r="10" fill="none" stroke="var(--icon)" stroke-width="2.2"/><circle cx="12" cy="12" r="6" fill="none" stroke="var(--icon)" stroke-width="1.6"/></svg>
    <div class="abs feature" style="left:304px;top:417px"><h4>280+ Install Scripts</h4><p>All our hosting accounts allow you to install popular software such as Pressly, Nodal, Jumla and Shoply in one easy step. Upgrading your software is just as easy!</p></div>

    <svg class="abs" style="left:79px;top:469px" width="22" height="22" viewBox="0 0 22 22"><path d="M3 19 L14 8 M8 3 L19 14" stroke="var(--icon)" stroke-width="2.4" stroke-linecap="round"/><circle cx="16" cy="5" r="3" fill="none" stroke="var(--icon)" stroke-width="1.8"/></svg>
    <div class="abs feature" style="left:110px;top:468px"><h4>HostPanel Included</h4><p>All hosting accounts come with the latest version of HostPanel. This makes life easy for you to do routine tasks such as setting up email addresses and managing SQL databases.</p></div>

    <svg class="abs" style="left:272px;top:469px" width="26" height="14" viewBox="0 0 26 14"><ellipse cx="13" cy="7" rx="12" ry="6" fill="var(--icon)"/></svg>
    <div class="abs feature" style="left:304px;top:468px"><h4>Latest Runtimes &amp; SQL</h4><p>Our network runs the latest stable and secure versions of script runtimes &amp; SQL servers. We also implement strict security and firewall rules protecting your website from unwanted visitors 24/7.</p></div>
  </section>

  <section>
    <div class="abs servers" role="img" aria-label="Illustration of three server towers with glowing blue lights"></div>
    <h2 class="abs lay-title">Features Layout</h2>
    <p class="abs lay-sub">A left aligned image and content with tick</p>
    <p class="abs lay-text">As soon as you make a successful payment via PayWell or QuickCheckout, your web hosting and domain names will be activated immediately. No waiting time whatsoever. Our network runs the latest stable and secure versions of runtimes &amp; SQL.</p>
    <div class="abs tick" style="left:240px;top:591px"><svg width="7" height="7" viewBox="0 0 10 10"><circle cx="5" cy="5" r="5" fill="var(--green)"/><path d="M2.6 5.2 L4.3 6.8 L7.4 3.6" stroke="#fff" stroke-width="1.4" fill="none"/></svg>Dedicated Servers</div>
    <div class="abs tick" style="left:240px;top:603px"><svg width="7" height="7" viewBox="0 0 10 10"><circle cx="5" cy="5" r="5" fill="var(--green)"/><path d="M2.6 5.2 L4.3 6.8 L7.4 3.6" stroke="#fff" stroke-width="1.4" fill="none"/></svg>SQL Databases</div>
    <div class="abs tick" style="left:240px;top:615px"><svg width="7" height="7" viewBox="0 0 10 10"><circle cx="5" cy="5" r="5" fill="var(--green)"/><path d="M2.6 5.2 L4.3 6.8 L7.4 3.6" stroke="#fff" stroke-width="1.4" fill="none"/></svg>Web Builder</div>
    <div class="abs tick" style="left:354px;top:591px"><svg width="7" height="7" viewBox="0 0 10 10"><circle cx="5" cy="5" r="5" fill="var(--green)"/><path d="M2.6 5.2 L4.3 6.8 L7.4 3.6" stroke="#fff" stroke-width="1.4" fill="none"/></svg>HostPanel Access</div>
    <div class="abs tick" style="left:354px;top:603px"><svg width="7" height="7" viewBox="0 0 10 10"><circle cx="5" cy="5" r="5" fill="var(--green)"/><path d="M2.6 5.2 L4.3 6.8 L7.4 3.6" stroke="#fff" stroke-width="1.4" fill="none"/></svg>Super Bandwidth</div>
    <div class="abs tick" style="left:354px;top:615px"><svg width="7" height="7" viewBox="0 0 10 10"><circle cx="5" cy="5" r="5" fill="var(--green)"/><path d="M2.6 5.2 L4.3 6.8 L7.4 3.6" stroke="#fff" stroke-width="1.4" fill="none"/></svg>Web Secutity</div>
  </section>

  <h2 class="abs section-title" style="top:654px">Testimonials</h2>
  <p class="abs section-sub" style="top:670px">Kind words from our valuable customers</p>

  <section>
    <div class="abs avatar" style="left:124px;top:696px"></div>
    <p class="abs quote" style="left:84px;top:727px">Peakhost servers are having high physical security and power redundancy Your data will be secure with us.</p>
    <p class="abs author" style="left:84px;top:754px">James, Tenvora</p>

    <div class="abs avatar" style="left:253px;top:696px"></div>
    <p class="abs quote" style="left:213px;top:727px">With our ultra mordern servers and optical cables, your data will be transfered to end user in milliseconds.</p>
    <p class="abs author" style="left:213px;top:754px">Mariya, Brightden</p>

    <div class="abs avatar" style="left:382px;top:696px"></div>
    <p class="abs quote" style="left:342px;top:727px">We have a dedicated team of support for sales and support to help you in anytime. You can also chat with us.</p>
    <p class="abs author" style="left:342px;top:754px">Steven, Gigsmith</p>

    <span class="abs partner" style="left:88px">Partner</span>
    <span class="abs partner" style="left:169px">Partner</span>
    <span class="abs partner" style="left:264px">Partner</span>
    <span class="abs partner" style="left:348px">Partner</span>
    <span class="abs partner" style="left:424px">Partner</span>
  </section>

  <h2 class="abs section-title" style="top:826px">Plans &amp; Pricing</h2>
  <p class="abs section-sub" style="top:842px">Tailored plans and pricing suits your needs</p>

  <section>
    <div class="abs plan" style="left:78px">
      <div class="plan-head"><h5>STANDARD</h5><span>Monthly Plan</span></div>
      <div class="price">$15</div>
      <ul class="plan-list"><li>1 GB Storage Space</li><li>10 GB Monthly Bandwidth</li><li>10 Sub-domains</li><li>25 Email Accounts</li><li>Control panel</li><li>24/7 Support</li></ul>
      <a class="plan-btn">Sign Up</a>
    </div>
    <div class="abs plan" style="left:175px">
      <div class="plan-head"><h5>DEDICATED</h5><span>Monthly Plan</span></div>
      <div class="price">$29</div>
      <ul class="plan-list"><li>5 GB Storage Space</li><li>50 GB Monthly Bandwidth</li><li>20 Sub-domains</li><li>50 Email Accounts</li><li>Control panel</li><li>24/7 Support</li></ul>
      <a class="plan-btn">Sign Up</a>
    </div>
    <div class="abs plan hot" style="left:272px">
      <div class="plan-head"><h5>MANAGED</h5><span>Monthly Plan</span></div>
      <div class="price">$67</div>
      <ul class="plan-list"><li>10 GB Storage Space</li><li>100 GB Monthly Bandwidth</li><li>Unlimited Sub-domains</li><li>Unlimited Email Accounts</li><li>Control panel</li><li>24/7 Support</li></ul>
      <a class="plan-btn">Sign Up</a>
    </div>
    <div class="abs plan" style="left:369px">
      <div class="plan-head"><h5>CLOUD / VPS</h5><span>Monthly Plan</span></div>
      <div class="price">$99</div>
      <ul class="plan-list"><li>20 GB Storage Space</li><li>200 GB Monthly Bandwidth</li><li>Unlimited Sub-domains</li><li>Unlimited Email Accounts</li><li>Control panel</li><li>24/7 Support</li></ul>
      <a class="plan-btn">Sign Up</a>
    </div>
  </section>

  <footer class="abs footer">
    <div class="abs fcol" style="left:79px"><h6>CALL US</h6>+41 44 555 0147<br>+41 44 555 0182</div>
    <div class="abs fcol" style="left:143px"><h6>FOLLOW US</h6>Follow on Chirper<br>Like us on Friendbook<br>Join on Linkwork</div>
    <div class="abs fcol" style="left:208px"><h6>EMAIL US</h6>support@peakhost.com<br>sales@peakhost.com</div>
    <div class="abs fcol" style="left:273px"><h6>COMPANY</h6>About us<br>Latest from Blog<br>Our Team</div>
    <div class="abs fcol" style="left:337px"><h6>LEGAL TERMS</h6>Terms of use<br>Privacy Policy</div>
    <div class="abs fcol" style="left:401px"><h6>LIVE CHAT</h6></div>
    <a class="abs chat">CHAT WITH US</a>
    <div class="abs fbrand">Peakhost</div>
  </footer>

</div>
</body>
</html>
```